Fitness website

Website for a fitness brand (see attached specs). Design needs to be modern and vibrant with CTAs on every page. We will provide logos, images, etc but for now user placeholder text and images. For now use the name 'Korveth Conditioning' as the name to use on the design. The goal of this site is to either get people to join the gym (5 physical locations across the US); buy an online program; buy merch or supplements or sign up for the newsletter. Pleas use images from this foldeR: https://files.morvanshare.example/folders/8QpLk27ZxTrWc93NbVe4HsYd1JuF0aMo?usp=sharing

We will be coding this in ReactNative. Lots more work for the winner as well, this is a 1st project for us.

Target Market(s)

fitness enthusiats

Industry/Entity Type

fitness, health, wellness

Number of Pages Required

5+ page

Font styles to use
Other font styles liked:
• Lato

Colors
0054AA
0677BA
7BADD7
CADEEF
E8F1F8
0094D4
00A9DD
6FCCEA
C7EBF8
E9F6FB
00AB8E
00BBA5
67D7C9
C6EFE9
E9F9F6
EE7325
F08F49
F5BC92
FAE3D3
FDF4ED

Requirements
Must have
• must be reactive. most people will view it first on mobile
Nice to have
• video in hero section of top of home page

```html
<!DOCTYPE html>
<html lang="en">
<head>
<meta charset="utf-8">
<title>Korveth Conditioning</title>
<link href="https://fonts.googleapis.com/css2?family=Teko:wght@400;500;600&family=Lato:wght@400;700&family=Russo+One&display=swap" rel="stylesheet">
<style>
:root{
  --orange:#EE7325;
  --orange-soft:#FAE3D3;
  --ink:#141414;
  --white:#ffffff;
}
*{margin:0;padding:0;box-sizing:border-box}
html,body{width:1200px;height:3905px;overflow:hidden;background:var(--white);font-family:'Lato',sans-serif;color:var(--ink)}
.page{position:relative;width:1200px;height:3905px;overflow:hidden}
.abs{position:absolute}
.teko{font-family:'Teko',sans-serif;font-weight:500;text-transform:uppercase;line-height:1}

/* hero */
.hero-photo{position:absolute;left:0;top:0;width:1200px;height:870px;background:linear-gradient(100deg,#0d0d0f 0%,#1c2026 35%,#2b3038 60%,#3a3630 80%,#1a1715 100%)}
.hero-shape{position:absolute;left:0;top:0}
.brand{position:absolute;left:52px;top:26px;font-family:'Teko',sans-serif;font-weight:500;font-size:36px;line-height:1;color:var(--orange);white-space:nowrap}
.nav{position:absolute;left:565px;top:21px;width:582px;height:63px;background:var(--orange);clip-path:polygon(0 0,100% 0,100% 100%,7% 100%)}
.nav-inner{position:absolute;left:0;top:0;width:582px;height:59px;background:var(--white);clip-path:polygon(0 0,100% 0,100% 100%,7.3% 100%);display:flex;align-items:center;padding-left:40px;padding-right:24px;justify-content:space-between}
.nav-inner a{font-family:'Teko',sans-serif;font-weight:500;font-size:17px;color:var(--ink);text-decoration:none;text-transform:uppercase;white-space:nowrap;padding-top:4px}
.nav-inner a.active{color:var(--orange)}
.hero-title{position:absolute;left:52px;top:256px;font-family:'Russo One',sans-serif;color:var(--white);font-size:58px;line-height:64px;text-transform:uppercase;font-weight:400}
.hero-sub{position:absolute;left:52px;top:400px;color:var(--white);font-size:32px;letter-spacing:.5px}
.btn{position:absolute;display:flex;align-items:center;justify-content:center;gap:8px;font-family:'Teko',sans-serif;font-size:19px;font-weight:500;text-transform:uppercase;color:var(--white);padding-top:3px;white-space:nowrap}
.btn-outline{left:52px;top:488px;width:109px;height:42px;border:1.5px solid var(--white)}
.btn-fill{left:188px;top:488px;width:145px;height:42px;background:var(--orange)}

/* newsletter */
.news-label{left:250px;top:905px;font-size:20px;white-space:nowrap}
.news-input{left:447px;top:895px;width:376px;height:43px;border:1.5px solid var(--orange);border-radius:3px;font-size:14px;color:#777;padding:13px 14px}
.news-btn{left:835px;top:897px;width:121px;height:40px;background:var(--ink);color:var(--white);font-size:15px;border-radius:3px;display:flex;align-items:center;justify-content:center;padding-top:3px}

/* sections */
.dark{position:absolute;left:0;width:1200px;background:var(--ink)}
.sec-title{position:absolute;left:0;width:1200px;text-align:center;font-size:46px;color:var(--orange)}
.sec-sub{position:absolute;left:0;width:1200px;text-align:center;font-size:14px}
.ph{position:absolute}
.feat-title{font-size:22px;color:var(--orange)}
.feat-text{font-size:14px;color:var(--white);line-height:21px;width:253px}

/* pricing */
.plan{position:absolute;top:1605px;width:347px;height:363px;background:var(--orange);border-radius:3px;color:var(--white);padding:20px 19px}
.plan h3{font-size:28px;font-weight:500;color:var(--white)}
.plan .term{font-size:15px}
.plan .price{font-size:35px;font-weight:700;margin-top:8px}
.plan .price small{font-size:17px}
.plan ul{list-style:none;margin-top:22px}
.plan li{display:flex;align-items:center;gap:10px;font-size:14px;height:48px;white-space:nowrap}
.plan .enroll{position:absolute;left:99px;top:295px;width:148px;height:41px;background:var(--ink);color:var(--white);font-size:16px;display:flex;align-items:center;justify-content:center;border-radius:3px;padding-top:3px}

/* map */
.map-bg{position:absolute;left:0;top:2467px;width:1200px;height:468px;background:linear-gradient(180deg,#f3f3f3,#ebebeb 50%,#f4f4f4)}
.area-panel{position:absolute;left:132px;top:2529px;width:220px;height:362px;background:rgba(150,150,150,.55)}
.area-copy{position:absolute;left:145px;top:2529px}
.area-copy h4{margin-top:36px;font-size:24px;font-weight:500}
.area-copy p{font-size:13px;line-height:20px;margin-top:4px;width:290px}
.area-copy li{list-style:none;display:flex;align-items:center;gap:10px;font-size:15px;height:38px}
.ring{width:16px;height:16px;border-radius:50%;border:2px solid #e8a079}
.zone{position:absolute;left:527px;top:2509px;width:376px;height:376px;border-radius:50%;background:rgba(238,115,37,.14);border:1.5px solid var(--orange)}
.pin{position:absolute;text-align:center;width:100px;font-size:15px;color:#222}

/* testimonials */
.review{position:absolute;top:3063px;width:347px;height:244px;background:var(--ink);color:var(--white);border-radius:2px;padding:22px 22px}
.review .head{display:flex;align-items:center;gap:12px}
.avatar{width:52px;height:52px;border-radius:50%;background:linear-gradient(135deg,#e9e9e9,#bfc4c9)}
.review .name{font-size:24px}
.review .when{font-size:13px}
.review .src{position:absolute;right:18px;top:36px;width:16px;height:16px;border-radius:50%;border:3px solid #4a8af4}
.stars{color:var(--white);font-size:14px;letter-spacing:1px;margin-top:14px}
.review p{font-size:14px;line-height:20.5px;margin-top:16px}
.dots{position:absolute;top:3332px;left:576px;display:flex;gap:5px}
.dots span{width:12px;height:12px;border-radius:50%;background:var(--orange)}

/* footer */
.f-contact{position:absolute;left:53px;font-size:16px;color:var(--white);display:flex;align-items:center;gap:6px;white-space:nowrap}
.f-ico{width:22px;height:22px;border-radius:50%;background:var(--white);display:flex;align-items:center;justify-content:center}
.f-nav{position:absolute;top:3524px;left:298px;display:flex}
.f-nav a{font-family:'Teko',sans-serif;font-size:15px;color:var(--white);text-decoration:none;text-transform:uppercase;margin-right:44px;white-space:nowrap}
.social{position:absolute;top:3617px;width:46px;height:46px;border-radius:50%;background:var(--white)}
.copy-rule{position:absolute;left:0;top:3830px;width:1200px;height:1px;background:rgba(255,255,255,.45)}
.copy{position:absolute;left:0;top:3861px;width:1200px;text-align:center;color:var(--white);font-size:15px}

.form{position:absolute;left:864px;top:3359px;width:308px;height:429px;background:var(--white);box-shadow:0 2px 10px rgba(0,0,0,.15)}
.form .kick{position:absolute;left:0;top:24px;width:308px;text-align:center;color:var(--orange);font-size:14px}
.form h4{position:absolute;left:0;top:50px;width:308px;text-align:center;font-size:32px;font-weight:500}
.field{position:absolute;left:22px;width:264px;border:1px solid #c9c9c9;border-radius:3px;font-size:13px;color:#999;padding:14px 13px}
.send{position:absolute;left:78px;top:359px;width:120px;height:42px;background:var(--ink);color:var(--white);font-size:16px;border-radius:3px;display:flex;align-items:center;justify-content:center;padding-top:3px}
</style>
</head>
<body>
<div class="page">

  <!-- hero -->
  <div class="hero-photo" role="img" aria-label="Athlete standing in a dim gym with weight plates and dumbbell racks"></div>
  <svg class="hero-shape" width="1200" height="870" viewBox="0 0 1200 870" aria-hidden="true">
    <path d="M0,727 Q600,910 1200,740 L1200,870 L0,870 Z" fill="#ffffff"/>
    <path d="M147,780 Q604,880 1061,780 Q604,935 147,780 Z" fill="#EE7325"/>
  </svg>
  <div class="brand">Korveth Conditioning</div>
  <nav class="nav"><div class="nav-inner">
    <a class="active" href="#">Home</a><a href="#">About us</a><a href="#">Packeges</a><a href="#">Products</a><a href="#">Gellary</a><a href="#">Contact</a>
    <svg width="18" height="16" viewBox="0 0 18 16" aria-label="Cart"><path d="M0 1h3l2.5 9h9L17 4H5" fill="none" stroke="#EE7325" stroke-width="2"/><circle cx="7" cy="13.5" r="1.6" fill="#EE7325"/><circle cx="13" cy="13.5" r="1.6" fill="#EE7325"/><path d="M5 4h12l-2.5 6h-9z" fill="#EE7325"/></svg>
  </div></nav>
  <h1 class="hero-title">Your best workout<br>starts today!</h1>
  <div class="hero-sub">FEEL THE BURN, LOVE THE RESULTS</div>
  <a class="btn btn-outline">Join now <svg width="16" height="12" viewBox="0 0 16 12"><path d="M0 6h14M9 1l5 5-5 5" fill="none" stroke="#fff" stroke-width="1.6"/></svg></a>
  <a class="btn btn-fill">Contact now <svg width="16" height="12" viewBox="0 0 16 12"><path d="M0 6h14M9 1l5 5-5 5" fill="none" stroke="#fff" stroke-width="1.6"/></svg></a>

  <!-- newsletter -->
  <div class="abs teko news-label">Sign up for the newsletter</div>
  <div class="abs news-input">Your Email</div>
  <div class="abs teko news-btn">Subscribe</div>

  <!-- why choose us -->
  <section class="dark" style="top:994px;height:453px"></section>
  <h2 class="sec-title teko" style="top:1024px">Why choose us</h2>
  <p class="sec-sub" style="top:1078px;color:#fff">Lorem Ipsum is simply dummy text of the printing and typesetting industry</p>
  <div class="ph" style="left:52px;top:1126px;width:253px;height:160px;background:linear-gradient(180deg,#d9dde0,#8d9297)" role="img" aria-label="Bright gym floor with training machines"></div>
  <div class="ph" style="left:335px;top:1126px;width:253px;height:160px;background:linear-gradient(180deg,#e8e4df,#6b5547)" role="img" aria-label="Healthy chia pudding cups"></div>
  <div class="ph" style="left:615px;top:1126px;width:253px;height:160px;background:linear-gradient(180deg,#1f1b18,#3d2a20)" role="img" aria-label="Athlete under a shower"></div>
  <div class="ph" style="left:895px;top:1126px;width:253px;height:160px;background:linear-gradient(180deg,#2b2b2b,#4a4a4a)" role="img" aria-label="Personal trainer portrait"></div>
  <div class="abs" style="left:52px;top:1310px"><div class="teko feat-title">Quality equipment</div><p class="feat-text" style="margin-top:6px">Lorem Ipsum is simply dummy text of the printing and typesetting industry</p></div>
  <div class="abs" style="left:335px;top:1310px"><div class="teko feat-title">Healthy nutrition plan</div><p class="feat-text" style="margin-top:6px">Lorem Ipsum is simply dummy text of the printing and typesetting industry</p></div>
  <div class="abs" style="left:615px;top:1310px"><div class="teko feat-title">Shower service</div><p class="feat-text" style="margin-top:6px">Lorem Ipsum is simply dummy text of the printing and typesetting industry</p></div>
  <div class="abs" style="left:895px;top:1310px"><div class="teko feat-title">Unique to your needs</div><p class="feat-text" style="margin-top:6px">Lorem Ipsum is simply dummy text of the printing and typesetting industry</p></div>

  <!-- pricing -->
  <h2 class="sec-title teko" style="top:1496px">Choose your pricing plan</h2>
  <p class="sec-sub" style="top:1543px">Lorem Ipsum is simply dummy text of the printing and typesetting industry</p>

  <div class="plan" style="left:50px">
    <h3 class="teko">Muscle build pro</h3><div class="term">1 YEAR TRAINING PROGRAM</div>
    <div class="price">$ 89.99/<small>1 YEARS</small></div>
    <ul>
      <li><svg width="18" height="18" viewBox="0 0 18 18"><rect x="1" y="2" width="14" height="14" rx="3" fill="none" stroke="#141414" stroke-width="1.6"/><path d="M5 9l3 3 8-9" fill="none" stroke="#141414" stroke-width="1.8"/></svg>Lorem ipsum dolor sit Praesent convallis</li>
      <li><svg width="18" height="18" viewBox="0 0 18 18"><rect x="1" y="2" width="14" height="14" rx="3" fill="none" stroke="#141414" stroke-width="1.6"/><path d="M5 9l3 3 8-9" fill="none" stroke="#141414" stroke-width="1.8"/></svg>Lorem ipsum dolor sit Praesent convallis</li>
      <li><svg width="18" height="18" viewBox="0 0 18 18"><rect x="1" y="2" width="14" height="14" rx="3" fill="none" stroke="#141414" stroke-width="1.6"/><path d="M5 9l3 3 8-9" fill="none" stroke="#141414" stroke-width="1.8"/></svg>Lorem ipsum dolor sit Praesent convallis</li>
    </ul>
    <a class="enroll teko">Enroll now</a>
  </div>
  <div class="plan" style="left:427px">
    <h3 class="teko">Women strength training</h3><div class="term">6 MONTHS TRAINING PROGRAM</div>
    <div class="price">$ 89.99/<small>1 YEARS</small></div>
    <ul>
      <li><svg width="18" height="18" viewBox="0 0 18 18"><rect x="1" y="2" width="14" height="14" rx="3" fill="none" stroke="#141414" stroke-width="1.6"/><path d="M5 9l3 3 8-9" fill="none" stroke="#141414" stroke-width="1.8"/></svg>Lorem ipsum dolor sit Praesent convallis</li>
      <li><svg width="18" height="18" viewBox="0 0 18 18"><rect x="1" y="2" width="14" height="14" rx="3" fill="none" stroke="#141414" stroke-width="1.6"/><path d="M5 9l3 3 8-9" fill="none" stroke="#141414" stroke-width="1.8"/></svg>Lorem ipsum dolor sit Praesent convallis</li>
      <li><svg width="18" height="18" viewBox="0 0 18 18"><rect x="1" y="2" width="14" height="14" rx="3" fill="none" stroke="#141414" stroke-width="1.6"/><path d="M5 9l3 3 8-9" fill="none" stroke="#141414" stroke-width="1.8"/></svg>Lorem ipsum dolor sit Praesent convallis</li>
    </ul>
    <a class="enroll teko">Enroll now</a>
  </div>
  <div class="plan" style="left:801px">
    <h3 class="teko">Fat burning pro</h3><div class="term">3 MONTHS TRAINING PROGRAM</div>
    <div class="price">$ 89.99/<small>1 YEARS</small></div>
    <ul>
      <li><svg width="18" height="18" viewBox="0 0 18 18"><rect x="1" y="2" width="14" height="14" rx="3" fill="none" stroke="#141414" stroke-width="1.6"/><path d="M5 9l3 3 8-9" fill="none" stroke="#141414" stroke-width="1.8"/></svg>Lorem ipsum dolor sit Praesent convallis</li>
      <li><svg width="18" height="18" viewBox="0 0 18 18"><rect x="1" y="2" width="14" height="14" rx="3" fill="none" stroke="#141414" stroke-width="1.6"/><path d="M5 9l3 3 8-9" fill="none" stroke="#141414" stroke-width="1.8"/></svg>Lorem ipsum dolor sit Praesent convallis</li>
      <li><svg width="18" height="18" viewBox="0 0 18 18"><rect x="1" y="2" width="14" height="14" rx="3" fill="none" stroke="#141414" stroke-width="1.6"/><path d="M5 9l3 3 8-9" fill="none" stroke="#141414" stroke-width="1.8"/></svg>Lorem ipsum dolor sit Praesent convallis</li>
    </ul>
    <a class="enroll teko">Enroll now</a>
  </div>

  <!-- showcase -->
  <section class="dark" style="top:2023px;height:444px"></section>
  <h2 class="sec-title teko" style="top:2056px;color:#fff">Showcase</h2>
  <p class="sec-sub" style="top:2107px;color:#fff">Lorem Ipsum is simply dummy text of the printing and typesetting industry</p>
  <div class="ph" style="left:52px;top:2167px;width:253px;height:242px;background:linear-gradient(160deg,#4b4038,#2a2a2c)" role="img" aria-label="Two athletes doing a kettlebell workout"></div>
  <div class="ph" style="left:333px;top:2167px;width:253px;height:242px;background:linear-gradient(160deg,#3a3d44,#6c625a)" role="img" aria-label="Athletes lifting barbells overhead"></div>
  <div class="ph" style="left:615px;top:2167px;width:253px;height:242px;background:linear-gradient(160deg,#2c2f33,#55504a)" role="img" aria-label="Athlete resting between sets"></div>
  <div class="ph" style="left:895px;top:2167px;width:253px;height:242px;background:linear-gradient(160deg,#2b3446,#6e6660)" role="img" aria-label="Athlete deadlifting a loaded barbell"></div>
  <svg class="abs" style="left:7px;top:2272px" width="32" height="32" viewBox="0 0 32 32" aria-label="Previous"><circle cx="16" cy="16" r="16" fill="#fff"/><path d="M19 9l-7 7 7 7" fill="none" stroke="#141414" stroke-width="2.6"/></svg>
  <svg class="abs" style="left:1158px;top:2272px" width="32" height="32" viewBox="0 0 32 32" aria-label="Next"><circle cx="16" cy="16" r="16" fill="#EE7325"/><path d="M13 9l7 7-7 7" fill="none" stroke="#fff" stroke-width="2.6"/></svg>

  <!-- service area -->
  <div class="map-bg" role="img" aria-label="Faded street map of the service area with a route line"></div>
  <div class="area-panel"></div>
  <div class="area-copy">
    <h4 class="teko">Service area</h4>
    <p>Lorem ipsum dolor sit amet, consectetuer .<br>Aenean commodo ligula eget dolor.</p>
    <ul style="margin-top:8px">
      <li><span class="ring"></span>Location 1</li>
      <li><span class="ring"></span>Location 2</li>
      <li><span class="ring"></span>Location 3</li>
      <li><span class="ring"></span>Location 4</li>
      <li><span class="ring"></span>Location 5</li>
    </ul>
  </div>
  <div class="zone"></div>
  <div class="pin" style="left:585px;top:2578px"><svg width="20" height="26" viewBox="0 0 20 26"><path d="M10 25C4 17 1 13 1 9a9 9 0 0 1 18 0c0 4-3 8-9 16z" fill="#EE7325"/><circle cx="10" cy="9" r="3.5" fill="#fff"/></svg><div>Location 1</div></div>
  <div class="pin" style="left:726px;top:2578px"><svg width="20" height="26" viewBox="0 0 20 26"><path d="M10 25C4 17 1 13 1 9a9 9 0 0 1 18 0c0 4-3 8-9 16z" fill="#EE7325"/><circle cx="10" cy="9" r="3.5" fill="#fff"/></svg><div>Location 2</div></div>
  <div class="pin" style="left:539px;top:2673px"><svg width="20" height="26" viewBox="0 0 20 26"><path d="M10 25C4 17 1 13 1 9a9 9 0 0 1 18 0c0 4-3 8-9 16z" fill="#EE7325"/><circle cx="10" cy="9" r="3.5" fill="#fff"/></svg><div>Location 3</div></div>
  <div class="pin" style="left:595px;top:2759px"><svg width="20" height="26" viewBox="0 0 20 26"><path d="M10 25C4 17 1 13 1 9a9 9 0 0 1 18 0c0 4-3 8-9 16z" fill="#EE7325"/><circle cx="10" cy="9" r="3.5" fill="#fff"/></svg><div>Location 4</div></div>
  <div class="pin" style="left:754px;top:2759px"><svg width="20" height="26" viewBox="0 0 20 26"><path d="M10 25C4 17 1 13 1 9a9 9 0 0 1 18 0c0 4-3 8-9 16z" fill="#EE7325"/><circle cx="10" cy="9" r="3.5" fill="#fff"/></svg><div>Location 5</div></div>

  <!-- testimonials -->
  <h2 class="sec-title teko" style="top:2987px">Voices of experience</h2>
  <div class="review" style="left:53px"><div class="head"><div class="avatar" role="img" aria-label="Reviewer photo"></div><div><div class="teko name">Jhon Doe</div><div class="when">4 month ago</div></div></div><span class="src"></span><div class="stars">★★★★★</div><p>Lorem Ipsum is simply dummy text of the printing and typesetting industryLorem Ipsum is simply dummy text of the printing and typesetting industry</p></div>
  <div class="review" style="left:427px"><div class="head"><div class="avatar" role="img" aria-label="Reviewer photo"></div><div><div class="teko name">Jhon Doe</div><div class="when">4 month ago</div></div></div><span class="src"></span><div class="stars">★★★★★</div><p>Lorem Ipsum is simply dummy text of the printing and typesetting industryLorem Ipsum is simply dummy text of the printing and typesetting industry</p></div>
  <div class="review" style="left:801px"><div class="head"><div class="avatar" role="img" aria-label="Reviewer photo"></div><div><div class="teko name">Jhon Doe</div><div class="when">4 month ago</div></div></div><span class="src"></span><div class="stars">★★★★★</div><p>Lorem Ipsum is simply dummy text of the printing and typesetting industryLorem Ipsum is simply dummy text of the printing and typesetting industry</p></div>
  <div class="dots"><span style="background:#141414"></span><span></span><span></span></div>

  <!-- footer -->
  <svg class="abs" style="left:0;top:0" width="1200" height="3905" viewBox="0 0 1200 3905" aria-hidden="true"><path d="M0,3394 Q600,3500 1200,3394 L1200,3905 L0,3905 Z" fill="#EE7325"/></svg>
  <div class="f-contact" style="top:3500px"><span class="f-ico"><svg width="12" height="12" viewBox="0 0 12 12"><path d="M2 1l2.2 0 1 2.6-1.3 1a6 6 0 0 0 3.5 3.5l1-1.3 2.6 1V10A1.5 1.5 0 0 1 9.5 11.5 9 9 0 0 1 .5 2.5 1.5 1.5 0 0 1 2 1z" fill="#141414"/></svg></span>0255019384</div>
  <div class="f-contact" style="top:3535px"><span class="f-ico"><svg width="12" height="10" viewBox="0 0 12 10"><rect x=".5" y=".5" width="11" height="9" rx="1" fill="#141414"/><path d="M1 1.5l5 4 5-4" fill="none" stroke="#fff" stroke-width="1"/></svg></span>info@korvethfit.example</div>
  <nav class="f-nav"><a href="#">Home</a><a href="#">About us</a><a href="#">Packeges</a><a href="#">Products</a><a href="#">Gellary</a><a href="#">Contact</a></nav>
  <a class="social" style="left:459px" aria-label="Social link one"></a>
  <a class="social" style="left:516px" aria-label="Social link two"></a>
  <a class="social" style="left:574px" aria-label="Social link three"></a>
  <div class="copy-rule"></div>
  <div class="copy">© 2025 Korveth Conditioning, All Rights Reserved</div>

  <div class="form">
    <div class="kick">let,s connect</div>
    <h4 class="teko">Contact us</h4>
    <div class="field" style="top:97px;height:44px">Frst Name</div>
    <div class="field" style="top:151px;height:43px">Email</div>
    <div class="field" style="top:206px;height:42px">Phone</div>
    <div class="field" style="top:259px;height:82px">Message</div>
    <div class="send teko">Send now</div>
  </div>

</div>
</body>
</html>
```